Book Cover - The Velvet Lantern Almanac Collection

We are writing a book about the velvet lantern almanac collection, including Guerrilla Marketing. Advertising, Branding and PR.

We are looking for a fun and quirky cover, and are open to your ideas 💡
My website and social media are on www.TorvanPelica.co and posts are shared on Trelvano. Again we are open to ideas

```html
<!DOCTYPE html>
<html lang="en">
<head>
<meta charset="utf-8">
<title>The Velvet Lantern Almanac Collection — Book Cover</title>
<link rel="stylesheet" href="https://fonts.googleapis.com/css2?family=Montserrat:ital,wght@0,600;0,700;1,500;1,800&display=swap">
<style>
  :root {
    --page-bg: #ffffff;
    --cover-bg: #ffffff;
    --ink: #231f20;
    --accent: #f4603e;
    --burst-yellow: #f7cf3a;
    --burst-orange: #f59a3b;
    --burst-red: #d9434a;
    --burst-plum: #8d5a86;
    --burst-lilac: #a99ac4;
    --burst-sky: #8ec7d8;
    --burst-blue: #4a86b0;
    --burst-teal: #3f9a8f;
    --burst-green: #7cbb57;
    --burst-lime: #c8d94a;
  }
  * { box-sizing: border-box; margin: 0; padding: 0; }
  html, body {
    width: 1200px;
    height: 1200px;
    overflow: hidden;
    background: var(--page-bg);
  }
  .canvas {
    position: relative;
    width: 1200px;
    height: 1200px;
    background: var(--page-bg);
  }
  .cover {
    position: absolute;
    left: 200px;
    top: 0;
    width: 800px;
    height: 1200px;
    background: var(--cover-bg);
    overflow: hidden;
    font-family: "Montserrat", sans-serif;
    color: var(--ink);
  }
  .cover__burst {
    position: absolute;
    left: -200px;
    top: -280px;
    width: 1200px;
    height: 1600px;
    background:
      radial-gradient(ellipse 330px 420px at 600px 800px, var(--cover-bg) 0%, var(--cover-bg) 62%, rgba(255,255,255,0.55) 78%, rgba(255,255,255,0) 100%),
      conic-gradient(from 0deg at 600px 800px,
        var(--burst-yellow) 0deg,
        var(--burst-orange) 30deg,
        var(--burst-red) 65deg,
        var(--burst-plum) 95deg,
        var(--burst-lilac) 120deg,
        var(--burst-sky) 140deg,
        var(--burst-blue) 170deg,
        var(--burst-teal) 200deg,
        var(--burst-green) 235deg,
        var(--burst-lime) 270deg,
        var(--burst-yellow) 300deg,
        var(--burst-orange) 330deg,
        var(--burst-yellow) 360deg);
    opacity: 0.75;
  }
  .cover__fade {
    position: absolute;
    left: 0;
    top: 1030px;
    width: 800px;
    height: 170px;
    background: linear-gradient(to bottom, rgba(255,255,255,0) 0%, var(--cover-bg) 45%);
  }
  .title {
    position: absolute;
    left: 0;
    top: 0;
    width: 800px;
    height: 800px;
  }
  .title__line {
    position: absolute;
    left: 0;
    width: 780px;
    text-align: center;
    white-space: nowrap;
    letter-spacing: -1px;
  }
  .title__the {
    top: 230px;
    left: -110px;
    font-weight: 700;
    font-size: 46px;
    letter-spacing: 0;
  }
  .title__velvet {
    top: 268px;
    left: -10px;
    font-style: italic;
    font-weight: 500;
    font-size: 116px;
    color: var(--accent);
  }
  .title__lantern {
    top: 386px;
    left: 10px;
    font-style: italic;
    font-weight: 500;
    font-size: 112px;
  }
  .title__almanac {
    top: 495px;
    left: 15px;
    font-style: italic;
    font-weight: 800;
    font-size: 108px;
  }
  .title__collection {
    top: 603px;
    left: 15px;
    font-style: italic;
    font-weight: 500;
    font-size: 104px;
    color: var(--accent);
  }
  .author {
    position: absolute;
    left: 0;
    top: 1124px;
    width: 800px;
    text-align: center;
    font-weight: 600;
    font-size: 37px;
    letter-spacing: 12px;
    padding-left: 12px;
  }
</style>
</head>
<body>
  <main class="canvas">
    <section class="cover">
      <div class="cover__burst" role="img" aria-label="Watercolour brush-stroke burst radiating in rainbow colours around the title"></div>
      <div class="cover__fade"></div>
      <h1 class="title">
        <span class="title__line title__the">The</span>
        <span class="title__line title__velvet">Velvet</span>
        <span class="title__line title__lantern">Lantern</span>
        <span class="title__line title__almanac">Almanac</span>
        <span class="title__line title__collection">Collection</span>
      </h1>
      <p class="author">AUTHOR NAME</p>
    </section>
  </main>
</body>
</html>
```